依頼概要
■依頼目的 / 概要
電子書籍Lumora本を出版いたしますので、
表紙デザイン作成をお願いいたします。

■納品物
下記での納品をお願い致します。

JPEG形式 及び PSD形式
横1600ピクセル x 縦2560ピクセル

■本の内容

<本のタイトル>
ソラノワ-SKY RING-
老職人に学んだ
はじめての家庭づくりのガイドブック

<著者名>
浅井徹郎

■デザイン要望
・本のタイトル / 著者名の反映をお願いします

デザインイメージ

・基本的に青系の色合い

・シンプルな背景にタイトル等のコピーを記載

・ターゲットは子どもを持つご両親。

・お子様の子育てに関する細かいノウハウというよりも、
最も要となる考え方をお伝えしています。

・信頼感のあるデザインを希望します。

<表現したいイメージなど>
・信頼感

<表現したくないイメージ>
・安っぽい
・嘘くさい
・大衆的

<利用画像について>
画像素材を使用される場合には、
商用利用可の素材をお願いします。

■その他
デザインを考えるのに必要な情報が他にございましたら、
お答えしますので、遠慮なくご連絡ください。

*添付ファイルは、過去電子書籍の表紙デザインです。
*ジャンルが異なりますので、デザインテイストは今回とは、異なります。
*あくまでも、表紙に出てくる要素(タイトルや著者名など)の参考としてご利用ください。

意図をしっかりとご理解いただき、
目につく素晴らしいデザインに仕上げていただきました。
ありがとうございます。

この度は応募いただきありがとうございました。
近いうちにまた同じく、表紙のデザインをお願いする予定です。
またご参加くださいませ。

```html
<!DOCTYPE html>
<html lang="ja">
<head>
<meta charset="utf-8">
<title>ソラノワ -SKY RING- 表紙</title>
<link rel="stylesheet" href="https://fonts.googleapis.com/css2?family=Montserrat:wght@800&family=Noto+Serif+JP:wght@700;900&family=Noto+Sans+JP:wght@500&display=swap">
<style>
  :root {
    --navy: #17168c;
    --royal: #2121b8;
    --shine: #8f93ff;
    --ink: #1a1a1a;
    --muted: #9a9a9a;
    --paper: #ffffff;
    --rule: rgba(255,255,255,0.75);
  }
  html, body { margin: 0; padding: 0; overflow: hidden; background: var(--paper); }
  .cover {
    position: relative;
    width: 746px; height: 1200px;
    background: var(--paper);
    overflow: hidden;
  }
  .top-band { position: absolute; left: 0; top: 0; width: 100%; height: 20px; background: var(--navy); }
  .wordmark { position: absolute; left: 0; top: 0; }
  .author {
    position: absolute; left: 236px; top: 498px;
    font-family: "Noto Serif JP", serif; font-weight: 900;
    color: var(--ink); font-size: 44px; letter-spacing: 2px; white-space: nowrap;
  }
  .author .suffix { font-size: 26px; font-weight: 700; margin-left: 22px; }
  .author-roman {
    position: absolute; left: 238px; top: 560px;
    font-family: "Noto Sans JP", sans-serif; font-weight: 500;
    font-size: 14px; color: var(--muted); letter-spacing: 1px;
  }
  .gem {
    position: absolute; left: 535px; top: 500px; width: 160px; height: 155px;
    border-radius: 50%;
    background: radial-gradient(circle at 45% 40%, #ffffff 0%, #d9dbe2 45%, #7f8290 80%, rgba(255,255,255,0) 100%);
  }
  .panel {
    position: absolute; left: 0; top: 668px; width: 100%; height: 532px;
    background: var(--navy); color: var(--paper);
    font-family: "Noto Serif JP", serif; font-weight: 700; text-align: center;
  }
  .lead { position: absolute; left: 0; width: 100%; top: 36px; font-size: 60px; letter-spacing: 2px; }
  .rule { position: absolute; left: 150px; width: 446px; height: 2px; background: var(--rule); }
  .rule.first { top: 124px; }
  .rule.second { top: 186px; }
  .middle { position: absolute; left: 0; width: 100%; top: 130px; font-size: 36px; }
  .subtitle { position: absolute; left: 0; width: 100%; top: 198px; font-size: 54px; letter-spacing: 1px; }
  .ghost-mark {
    position: absolute; left: 0; width: 100%; top: 335px;
    font-family: "Montserrat", sans-serif; font-weight: 800; font-size: 110px;
    color: transparent; -webkit-text-stroke: 1.5px rgba(255,255,255,0.08); letter-spacing: 6px;
  }
</style>
</head>
<body>
<div class="cover">
  <div class="top-band"></div>

  <svg class="wordmark" width="746" height="500" viewBox="0 0 746 500" aria-label="SKY RING ソラノワ">
    <defs>
      <linearGradient id="titleFill" x1="0" y1="0" x2="1" y2="1">
        <stop offset="0" stop-color="var(--navy)"/>
        <stop offset="0.18" stop-color="#2a2ad0"/>
        <stop offset="0.3" stop-color="#8f93ff"/>
        <stop offset="0.42" stop-color="#2323c0"/>
        <stop offset="1" stop-color="var(--navy)"/>
      </linearGradient>
    </defs>
    <g font-family="Montserrat, sans-serif" font-weight="800" font-size="250" fill="url(#titleFill)">
      <text x="70" y="300" textLength="400" lengthAdjust="spacingAndGlyphs">SK</text>
      <text x="552" y="300" textLength="133" lengthAdjust="spacingAndGlyphs">Y</text>
      <text x="70" y="485" textLength="615" lengthAdjust="spacingAndGlyphs">RING</text>
    </g>
    <text x="510" y="130" font-family="Noto Sans JP, sans-serif" font-weight="500" font-size="24"
          fill="#3e3ed0" style="writing-mode: vertical-rl" letter-spacing="10">ソラノワ</text>
  </svg>

  <div class="author">浅井 徹郎<span class="suffix">著</span></div>
  <div class="author-roman">Asai Tetsuro</div>
  <div class="gem" role="img" aria-label="輝くダイヤモンドの画像"></div>

  <section class="panel">
    <div class="lead">老職人に学んだ</div>
    <div class="rule first"></div>
    <div class="middle">はじめての</div>
    <div class="rule second"></div>
    <div class="subtitle">家庭づくりのガイドブック</div>
    <div class="ghost-mark">SKY RING</div>
  </section>
</div>
</body>
</html>
```